Concierge Healthcare Business Card Design and Logo

We need a logo and business card design for a new company called "Sound Keeper". We will provide concierge audiological care, hearing aids, hearing exams, custom hearing protection etc to patients in the comfort of their homes and offices. We would like a sleek and modern design preferably with an Ear related logo.

Target Market(s)

People with hearing loss, Hunters, Musicians
My usual clientele are older individuals so usually 50+ years old

Industry/Entity Type

Health Care

Contact Information for Business Card

Clara Whitfield, AuD
Audiologist
512-418-2967
soundkeeper@mailvista.net
www.soundkeeperclinic.net

Logo Text

Sound Keeper

Number of Pages Required

3 page

```html
<!DOCTYPE html>
<html lang="en">
<head>
<meta charset="utf-8">
<title>Sound Keeper – Business Card</title>
<link href="https://fonts.googleapis.com/css2?family=Lato:wght@400;700&display=swap" rel="stylesheet">
<style>
  :root {
    --ink: #414649;
    --paper: #ffffff;
    --rule: #8c8f91;
  }
  html, body {
    margin: 0;
    padding: 0;
    width: 1200px;
    height: 1114px;
    overflow: hidden;
    background: var(--paper);
    font-family: "Lato", sans-serif;
  }
  .canvas {
    position: relative;
    width: 1200px;
    height: 1114px;
  }
  .card {
    position: absolute;
    left: 180px;
    width: 838px;
    height: 479px;
    box-sizing: border-box;
  }
  .card--front {
    top: 56px;
    background: var(--ink);
    color: var(--paper);
  }
  .card--back {
    top: 577px;
    background: var(--paper);
    border: 1px solid var(--rule);
    color: var(--ink);
  }
  .brand-dot {
    position: absolute;
    border-radius: 50%;
  }
  .card--front .brand-dot {
    width: 120px;
    height: 120px;
    left: 376px;
    top: 146px;
    background: var(--paper);
  }
  .card--back .brand-dot {
    width: 100px;
    height: 100px;
    left: 168px;
    top: 162px;
    background: var(--ink);
  }
  .brand-name {
    position: absolute;
    margin: 0;
    font-weight: 400;
    letter-spacing: 0.06em;
    line-height: 1;
    white-space: nowrap;
    text-transform: uppercase;
  }
  .card--front .brand-name {
    left: 0;
    right: 0;
    top: 310px;
    text-align: center;
    font-size: 46px;
  }
  .card--back .brand-name {
    left: 30px;
    width: 380px;
    top: 294px;
    text-align: center;
    font-size: 36px;
  }
  .divider {
    position: absolute;
    left: 404px;
    top: 118px;
    width: 2px;
    height: 243px;
    background: var(--ink);
  }
  .contact {
    position: absolute;
    left: 449px;
    top: 126px;
    margin: 0;
    line-height: 1;
  }
  .contact-name {
    font-size: 31px;
    font-weight: 700;
    margin: 0;
  }
  .contact-name .credential {
    font-weight: 400;
  }
  .contact-role {
    font-size: 25px;
    margin: 8px 0 0;
  }
  .contact-lines {
    list-style: none;
    padding: 0;
    margin: 31px 0 0;
    font-size: 24px;
  }
  .contact-lines li {
    margin: 0 0 14px;
  }
</style>
</head>
<body>
<main class="canvas">
  <section class="card card--front" aria-label="Card front">
    <span class="brand-dot" aria-hidden="true"></span>
    <h1 class="brand-name">Sound Keeper</h1>
  </section>

  <section class="card card--back" aria-label="Card back">
    <span class="brand-dot" aria-hidden="true"></span>
    <p class="brand-name">Sound Keeper</p>
    <span class="divider" aria-hidden="true"></span>
    <address class="contact" style="font-style:normal">
      <p class="contact-name">Clara Whitfield, <span class="credential">AuD</span></p>
      <p class="contact-role">Audiologist</p>
      <ul class="contact-lines">
        <li>512-418-2967</li>
        <li>soundkeeper@mailvista.net</li>
        <li>www.soundkeeperclinic.net</li>
      </ul>
    </address>
  </section>
</main>
</body>
</html>
```